Brellin Trade Partners - we are Asian sourcing agents

We are sourcing agents based in the USA and we act as sourcing agents for clients in throughout the world. We focus primarily on custom sewn goods. So basically companies who do not have the in-house expertise to do it themselves, come to us and have us find suitable factories in Asia to do the production. We are middlemen. We find the factories...quote the project...manage the quality control and then deliver the goods directly to our customer's door. We pride ourselves in making the communication very easy and precise.

Current page is www.brellintrade.example

I am not happy w/ the overall look. The spacing...the photos, the fonts...the design elements...the pictures. I want a cool, crisp design that conveys professionalism and clearly depicts/explains what we do.

Requirements
Must have
• use my logo....I like it...it was designed by someone on this website.
Nice to have
• a video/animation of the entire process would be wonderful. Showing initial contact with our office in the USA...then to my correspondence with my offices in Taiwan and in Hong Kong...and then back and fort w/ the customer.....and then between my people in Hong Kong/Taiwan with the local factories......and then a quote is generated and sent to my client......to samples being made and sent for approval.....to a PO being generated......to final samples being sent.....to the order being shipped and delivered to the clients warehouse. I was thinking of an animation showing arrows and text showing the back and forth communication and explaining how the process flows.

```html
<!DOCTYPE html>
<html lang="en">
<head>
<meta charset="utf-8">
<title>Brellin Trade Partners – Asian Outsourcing Made Easy</title>
<link rel="stylesheet" href="https://fonts.googleapis.com/css2?family=Archivo:wght@400;800;900&family=Roboto:wght@300;400;500;700&display=swap">
<style>
:root{
  --navy:#15205a;
  --navy-deep:#101a47;
  --olive:#8da326;
  --ink:#222;
  --muted:#8a8a8a;
  --rule:#d9d9d9;
  --footer-bg:#f2f3f8;
  --white:#fff;
}
*{box-sizing:border-box;margin:0;padding:0}
html,body{width:1200px;height:3341px;overflow:hidden}
body{position:relative;background:var(--white);font-family:"Roboto",Arial,sans-serif;color:var(--ink)}
.abs{position:absolute}

/* Hero */
.hero{left:0;top:0;width:1200px;height:821px;background:linear-gradient(180deg,#cfc7b8 0%,#e6e1d6 35%,#d8d3ca 70%,#b9b4ad 100%)}
.topbar{right:150px;top:6px;display:flex;align-items:center;gap:22px;font:700 24px "Roboto",Arial,sans-serif;color:var(--navy)}
.topbar .social{display:flex;gap:22px}
.topbar .social span{width:16px;height:16px;border-radius:50%;background:var(--navy);display:block}
.brand{left:124px;top:74px;font:800 34px/1 "Archivo",Arial,sans-serif;color:var(--olive);letter-spacing:.5px;width:300px}
.brand small{display:block;font:800 34px/1 "Archivo",Arial,sans-serif;margin-top:4px}
.nav{left:450px;top:86px;display:flex;gap:44px;font:500 19px "Roboto",Arial,sans-serif;color:var(--olive);letter-spacing:.5px}
.nav a{color:inherit;text-decoration:none}
.nav a.active{color:var(--navy)}
.hero-title{left:0;width:1200px;top:362px;text-align:center;font:900 54px/1 "Archivo",Arial,sans-serif;color:var(--navy-deep);letter-spacing:1px}
.hero-sub{left:0;width:1200px;top:420px;text-align:center;font:400 28px/1 "Roboto",Arial,sans-serif;color:var(--olive)}
.btn{display:flex;align-items:center;justify-content:center;background:var(--navy-deep);color:var(--white);text-transform:uppercase;font-family:"Roboto",Arial,sans-serif}
.hero-btn{left:468px;top:506px;width:256px;height:44px;font-size:22px;letter-spacing:1px}
.dots{left:14px;top:802px;display:flex;gap:8px}
.dots span{width:9px;height:9px;border-radius:50%;background:#fff;opacity:.6}
.dots span:first-child{opacity:1}
.arrows{right:0;top:782px;display:flex;gap:2px}
.arrows span{width:48px;height:39px;background:var(--navy-deep);display:flex;align-items:center;justify-content:center}

/* Sections */
.section-title{left:0;width:1200px;text-align:center;font:400 36px/1 "Roboto",Arial,sans-serif;color:var(--navy);letter-spacing:.5px}
.lead{left:231px;width:738px;top:924px;text-align:center;font:300 15px/1.55 "Roboto",Arial,sans-serif;color:var(--muted)}
.divider{left:223px;width:754px;height:1px;background:var(--rule)}
.read-more{width:112px;height:22px;font-size:12px;letter-spacing:.5px}

.quote-title{left:223px;top:1126px;font:400 24px "Roboto",Arial,sans-serif;color:var(--navy)}
.quote-bar{left:223px;top:1165px;width:30px;height:2px;background:var(--olive)}
.quote-text{left:223px;top:1186px;width:200px;font:300 16px/1.4 "Roboto",Arial,sans-serif;color:var(--muted)}
.quote-btn{left:217px;top:1295px;width:209px;height:36px;font-size:15px;border-radius:3px}
.photo{display:block}
.factory-photo{left:468px;top:1100px;width:506px;height:292px;background:linear-gradient(160deg,#2d3540 0%,#5c6670 45%,#3b4450 100%)}

.video{left:223px;top:1478px;width:751px;height:382px;background:linear-gradient(170deg,#5a6c86 0%,#7e8fa4 45%,#3d4c66 100%)}
.play{left:572px;top:1646px}
.controls{left:236px;top:1829px;width:725px;height:20px;display:flex;align-items:center;gap:12px;color:#fff;font-size:12px}
.controls .track{flex:1;height:4px;background:rgba(255,255,255,.45);position:relative}
.controls .track::before{content:"";position:absolute;left:0;top:0;width:3%;height:4px;background:#fff}

.sourcing-title{left:223px;top:1930px;font:400 27px "Roboto",Arial,sans-serif;color:var(--navy)}
.col-text{font:300 13px/1.5 "Roboto",Arial,sans-serif;color:var(--muted)}
.col-a{left:223px;top:1990px;width:420px}
.col-b{left:671px;top:1990px;width:303px}

.services{left:220px;top:2270px;width:780px;display:flex;justify-content:space-between}
.service{display:flex;align-items:center;gap:18px;font:400 22px "Roboto",Arial,sans-serif;color:var(--olive)}
.view-more{left:0;width:1200px;top:2418px;text-align:center;font:400 13px "Roboto",Arial,sans-serif;color:var(--navy-deep);letter-spacing:.5px}

.categories{left:173px;top:2492px;width:854px;height:250px}
.cat{position:absolute;height:125px}
.cat-label{left:0;top:0;width:164px;background:#fff;display:flex;align-items:center;justify-content:center;text-align:center;font:400 24px/1.15 "Roboto",Arial,sans-serif;color:var(--navy)}
.cat-medical{background:var(--navy);color:#fff;display:flex;flex-direction:column;align-items:center;justify-content:center;font:400 25px "Roboto",Arial,sans-serif;gap:6px}

/* Footer */
.footer-links{left:0;top:2812px;width:1200px;height:312px;background:var(--footer-bg)}
.fcol{position:absolute}
.fcol h4{font:500 16px "Roboto",Arial,sans-serif;color:var(--navy);margin-bottom:8px;letter-spacing:.3px}
.fcol ul{list-style:none;font:300 11.5px/1.5 "Roboto",Arial,sans-serif;color:var(--muted)}
.contact{left:0;top:3124px;width:1200px;height:128px;background:var(--navy-deep);color:#fff;font:400 14px/1.35 "Roboto",Arial,sans-serif}
.contact .item{position:absolute;display:flex;align-items:center;gap:14px}
.copyright{left:0;width:1200px;top:3272px;text-align:center;font:300 11px "Roboto",Arial,sans-serif;color:#666}
</style>
</head>
<body>

<header>
  <div class="abs hero photo" role="img" aria-label="Busy station concourse with blurred travellers under tall arched windows"></div>
  <div class="abs topbar">
    <span>555-010-4815</span>
    <div class="social"><span></span><span></span><span></span><span></span></div>
  </div>
  <div class="abs brand">BRELLIN<small>TRADE PARTNERS</small></div>
  <nav class="abs nav">
    <a class="active" href="#">HOME</a>
    <a href="#">PRODUCT CATEGORIES</a>
    <a href="#">ABOUT US</a>
    <a href="#">REQUEST QUOTE</a>
  </nav>
  <h1 class="abs hero-title">ASIAN OUTSOURCING MADE EASY!</h1>
  <p class="abs hero-sub">CUSTOM SEWN GOODS MADE TO YOUR SPECIFICATIONS</p>
  <a class="abs btn hero-btn">Request a Quote</a>
  <div class="abs dots"><span></span><span></span></div>
  <div class="abs arrows">
    <span><svg width="14" height="20" viewBox="0 0 14 20"><path d="M11 2 3 10l8 8" fill="none" stroke="#fff" stroke-width="2.5"/></svg></span>
    <span><svg width="14" height="20" viewBox="0 0 14 20"><path d="m3 2 8 8-8 8" fill="none" stroke="#fff" stroke-width="2.5"/></svg></span>
  </div>
</header>

<main>
  <h2 class="abs section-title" style="top:846px">WHAT WE DO</h2>
  <p class="abs lead">We aren't tied to a particular sewing factory in China, India, Korea, Vietnam, &amp; Thailand. We instead have a long-established network of factories with whom we have gained trust and understanding. This arrangement allows us access to many specialized areas of expertise &amp; virtually unlimited capacity. Simply put, through our experience as a sewing contractor we know which factories to use for each specific job.</p>
  <div class="abs divider" style="top:1055px"></div>
  <a class="abs btn read-more" style="left:532px;top:1044px">Read More</a>

  <h3 class="abs quote-title">REQUEST QUOTE</h3>
  <div class="abs quote-bar"></div>
  <p class="abs quote-text">Please contact us for immediate consultation regarding your outsourcing project.</p>
  <a class="abs btn quote-btn">Request Quote</a>
  <div class="abs factory-photo photo" role="img" aria-label="Large sewing factory floor with rows of workstations"></div>

  <div class="abs video photo" role="img" aria-label="Video of workers at sewing machines in a factory"></div>
  <svg class="abs play" width="48" height="48" viewBox="0 0 48 48"><circle cx="24" cy="24" r="22" fill="none" stroke="#fff" stroke-width="3"/><path d="M19 14v20l15-10z" fill="#fff"/></svg>
  <div class="abs controls">
    <svg width="14" height="16" viewBox="0 0 14 16"><rect x="1" y="1" width="4" height="14" fill="#fff"/><rect x="9" y="1" width="4" height="14" fill="#fff"/></svg>
    <span>1:23</span><div class="track"></div><span>3:00</span>
  </div>

  <h2 class="abs sourcing-title">SOURCING CUSTOM GOODS IN CHINA</h2>
  <p class="abs col-text col-a">We outsource sewing services direct from China. Our long established and extensive network of offshore factory-partners provides our clients with access to a wide variety of contract sewing expertise from Chinese manufacturers.</p>
  <p class="abs col-text col-b">Clients only need to communicate with our US agency, but will have the benefits of the cost savings &amp; quality workmanship from offshore outsourcing from Asia.</p>
  <div class="abs divider" style="top:2108px"></div>
  <a class="abs btn read-more" style="left:532px;top:2097px">Read More</a>

  <h2 class="abs section-title" style="top:2180px">OUR SERVICES</h2>
  <div class="abs services">
    <div class="service">
      <svg width="52" height="46" viewBox="0 0 52 46"><path d="M16 16v-4a10 10 0 0 1 20 0v4" fill="none" stroke="var(--navy)" stroke-width="4"/><rect x="2" y="16" width="48" height="28" rx="10" fill="var(--navy)"/></svg>Bags
    </div>
    <div class="service">
      <svg width="48" height="42" viewBox="0 0 48 42"><path d="M17 10V4h14v6" fill="none" stroke="var(--navy)" stroke-width="4"/><rect x="2" y="10" width="44" height="30" rx="3" fill="var(--navy)"/><rect x="2" y="22" width="44" height="3" fill="#fff"/><rect x="20" y="19" width="8" height="9" fill="var(--navy)" stroke="#fff" stroke-width="2"/></svg>Cases
    </div>
    <div class="service">
      <svg width="44" height="44" viewBox="0 0 44 44"><path d="M2 6l19 4v32L2 38z M42 6l-19 4v32l19-4z" fill="var(--navy)"/></svg>Covers
    </div>
    <div class="service">
      <svg width="46" height="46" viewBox="0 0 46 46"><path d="M16 8V4h14v4" fill="none" stroke="var(--navy)" stroke-width="3"/><rect x="3" y="8" width="40" height="36" rx="4" fill="none" stroke="var(--navy)" stroke-width="4"/><path d="M20 16h6v7h7v6h-7v7h-6v-7h-7v-6h7z" fill="var(--navy)"/></svg>Medical
    </div>
  </div>
  <p class="abs view-more">VIEW MORE SERVICES</p>

  <div class="abs categories">
    <div class="cat cat-label">PRODUCT<br>CATEGORIES</div>
    <div class="cat photo" style="left:164px;top:0;width:167px;background:linear-gradient(135deg,#c9a77a,#8a6a45)" role="img" aria-label="Spools of thread"></div>
    <div class="cat photo" style="left:331px;top:0;width:167px;background:linear-gradient(135deg,#e9e6e0,#c98a45)" role="img" aria-label="Orange leather handbag"></div>
    <div class="cat photo" style="left:498px;top:0;width:167px;background:linear-gradient(135deg,#f4f4f4,#2a2a2a)" role="img" aria-label="Pair of black work gloves"></div>
    <div class="cat photo" style="left:665px;top:0;width:189px;background:linear-gradient(135deg,#2b1f5a,#d4387d 50%,#38a8d6)" role="img" aria-label="Colourful phone cases"></div>
    <div class="cat photo" style="left:0;top:125px;width:290px;background:linear-gradient(135deg,#9aa0a6,#4a5058)" role="img" aria-label="Bicycle with cover"></div>
    <div class="cat cat-medical" style="left:290px;top:125px;width:287px">MEDICAL
      <svg width="30" height="30" viewBox="0 0 30 30"><circle cx="12" cy="12" r="9" fill="none" stroke="#fff" stroke-width="2.5"/><path d="m19 19 9 9M8 12h8M12 8v8" stroke="#fff" stroke-width="2.5"/></svg>
    </div>
    <div class="cat photo" style="left:577px;top:125px;width:277px;background:linear-gradient(135deg,#b86a2e,#2e3b63 55%,#e9e9e9)" role="img" aria-label="Assorted sports balls"></div>
  </div>
</main>

<footer>
  <div class="abs footer-links">
    <div class="fcol" style="left:167px;top:38px">
      <h4>CUSTOM BAGS</h4>
      <ul><li>Athletic Bags</li><li>Backpacks</li><li>Computer Bags</li><li>Cooler Bags</li><li>Cosmetic Bags</li><li>Handbags</li><li>Messenger Bags</li><li>Shopping Bags</li><li>Tool Bags</li><li>Travel Bags</li><li>Yoga Bags</li></ul>
    </div>
    <div class="fcol" style="left:367px;top:38px">
      <h4>CUSTOM COVERS</h4>
      <ul><li>ATV Covers</li><li>Chair Covers</li><li>Equipment Covers</li><li>Golf Cart Covers</li><li>Motorcycle Covers</li><li>Outdoor Furniture</li><li>Covers</li><li>Outdoor Grill Cover</li><li>Personal Watercraft</li><li>Covers</li><li>Snowmobile Covers</li></ul>
    </div>
    <div class="fcol" style="left:599px;top:38px">
      <h4>CUSTOM GLOVES</h4>
      <ul><li>Batting Gloves</li><li>Garden Gloves</li><li>Mechanic Gloves</li><li>Safety Gloves</li><li>Ski Gloves</li></ul>
    </div>
    <div class="fcol" style="left:599px;top:172px">
      <h4>CUSTOM CASES</h4>
      <ul><li>Cosmetic Cases</li><li>Phone Cases</li><li>Tool Bags and Tool</li><li>Cases</li></ul>
    </div>
    <div class="fcol" style="left:813px;top:38px">
      <h4>CUSTOM SEWN GOODS</h4>
      <ul><li>Pet Collars, Leashes, &amp;</li><li>Harnesses</li><li>Socks</li></ul>
    </div>
    <div class="fcol" style="left:813px;top:172px">
      <h4>CUSTOM SPORTING GOODS</h4>
      <ul><li>Yoga Mats</li><li>Yoga Gear and</li><li>Accessories</li></ul>
    </div>
  </div>

  <div class="abs contact">
    <div class="item" style="left:163px;top:44px">
      <svg width="26" height="36" viewBox="0 0 26 36"><path d="M13 1C6 1 1 6 1 13c0 9 12 22 12 22s12-13 12-22C25 6 20 1 13 1z" fill="var(--olive)"/><circle cx="13" cy="13" r="4.5" fill="var(--navy-deep)"/></svg>
      <span>12 Harbor Lane Unit B-4<br>Eastfield, NH 03000</span>
    </div>
    <div class="item" style="left:405px;top:50px">
      <svg width="30" height="30" viewBox="0 0 30 30"><path d="M7 2l5 7-3 3c2 4 5 7 9 9l3-3 7 5-3 5C13 28 2 17 2 5z" fill="var(--olive)"/></svg>
      <span>555-010-4815</span>
    </div>
    <div class="item" style="left:598px;top:50px">
      <svg width="30" height="28" viewBox="0 0 30 28"><rect x="8" y="1" width="14" height="8" fill="var(--olive)"/><rect x="1" y="9" width="28" height="12" rx="2" fill="var(--olive)"/><rect x="8" y="17" width="14" height="10" fill="var(--olive)" stroke="var(--navy-deep)" stroke-width="2"/></svg>
      <span>555-010-4363</span>
    </div>
    <div class="item" style="left:778px;top:50px">
      <svg width="34" height="28" viewBox="0 0 34 28"><path d="M1 12 33 1 24 27l-7-9-7 6 2-9z" fill="var(--olive)"/></svg>
      <span>Email: info@brellintrade.example</span>
    </div>
  </div>

  <p class="abs copyright">© 2015 Brellin Trade Partners, LLC | USA – Hong Kong – Taipei</p>
</footer>

</body>
</html>
```